Rise Forward: Leave Behind Old Patterns, Quit Drifting Through Days, Begin Shaping each Morning

Good day! I am excited to work again with you, amazing designers! This time I am looking for the cover design of my book.
Dimensions 6” x 9”
The book name is as my name project. I love simplicity, but yet that is impactful. I love colours, I don't have a specific colour in mind, but I like the mustard colour as the one in the logo of my company. I am open to ideas! I have attached some cover samples that I like so that it gives a better idea of what I have on mind.
I am looking for something that looks professional, yet, not super serious, that it's approachable to people. Something that calls their attention at first glance.
I am working with my editor and my interior designer as well to finalize this part of the book. I will be working with the person that I select for the book design to finalize it.
About the book, here a passage of an unedited version of the introduction for guidance :
My intention is to take you on a journey to help you to understand what is going on in your mind so that you get out from anything that is holding you back in your life. My intention is to guide you to start fully living and experiencing a life that your mind even have yet conceived. To experience a life where you live fearless and without suffering. Living your life where you are the navigator and the creator of how you are experiencing it and you are living in a world of possibilities where there are no limitations.
For it, we will start to understand more about the mind and about the brain. I am not a neuroscientist and neither I consider my self an expert in the workings of the brain, what I know is the result of my fascination about our brain. This curiosity and the part of me that likes to understand how things work took me to read, research and learn about how our brain works and how its intrinsic mechanisms are subconsciously influencing and limiting us. I encourage you to stay on this part, it can be a bit technical, but understanding how it works will empower you not to allow your mind to dictate the way you approach your life and to live on autopilot.
We will continue to describe how you have been programmed throughout your life, putting you inside a box limited by your subconscious beliefs and ideas about the world. In this part, we will also discuss what ego is, how it is subconsciously limiting you and how the ways of when ego manifests itself are limiting you and making you suffer. Now that you know how you have been enclosed in your mind for all your life, we will move to discuss how you can get out of it. You will learn how to master your emotions to eliminate your suffering and not allow them to control the direction of your life and use them as a mechanism to get out from your programed mind. We continue to discuss how to leverage the power of your mind and harness your power of choice. Finally, I invite you to see yourself as a holistic being so that you start truly living and take control over the direction of your life, by nourishing and taking care of all those aspects of you utilizing their wisdom and synergy to achieve higher connection within yourself, your soul and live your life in a higher level of consciousness with peace, flow, love and purpose.

```html
<!DOCTYPE html>
<html lang="en">
<head>
<meta charset="utf-8">
<title>Rise Forward – Book Cover</title>
<link rel="stylesheet" href="https://fonts.googleapis.com/css2?family=Montserrat:wght@800&family=Raleway:wght@700&family=Mulish:wght@400&family=Oswald:wght@500;700&display=swap">
<style>
  :root {
    --mustard: #fbbf18;
    --navy: #0e1a6b;
    --white: #ffffff;
    --ink: #1b1b2a;
  }
  html, body { margin: 0; padding: 0; overflow: hidden; background: var(--mustard); }
  .cover {
    position: relative; width: 1200px; height: 874px; overflow: hidden;
    background: var(--mustard); color: var(--navy);
  }
  .abs { position: absolute; }

  /* Back cover */
  .back-emblem { left: 266px; top: 18px; width: 48px; height: 58px; }
  .back-title {
    left: 0; width: 579px; top: 76px; text-align: center;
    font-family: "Montserrat", sans-serif; font-weight: 800; line-height: .9;
    letter-spacing: -1px;
  }
  .back-title .word-top { display: block; font-size: 44px; }
  .back-title .word-bottom { display: block; font-size: 38px; }
  .intro {
    left: 36px; top: 206px; width: 522px; margin: 0;
    font-family: "Mulish", sans-serif; font-size: 11.6px; line-height: 15.8px;
    color: var(--ink); text-align: justify;
  }
  .intro p { margin: 0 0 15px; }
  .divider { left: 65px; top: 449px; width: 493px; height: 1px; background: var(--navy); opacity: .6; }
  .about-heading {
    left: 79px; top: 458px; margin: 0;
    font-family: "Oswald", sans-serif; font-weight: 500; font-size: 27px;
    letter-spacing: 13.5px; color: var(--navy);
  }
  .author-photo { left: 54px; top: 527px; width: 129px; height: 149px; }
  .bio {
    left: 206px; top: 521px; width: 352px; margin: 0;
    font-family: "Mulish", sans-serif; font-size: 11.6px; line-height: 15.8px;
    color: var(--ink); text-align: justify;
  }
  .studio-mark {
    left: 25px; top: 784px; width: 163px; height: 61px; background: var(--white);
    display: flex; align-items: center; gap: 8px; padding-left: 12px; box-sizing: border-box;
  }
  .studio-mark .dot { width: 20px; height: 20px; background: var(--navy); flex: none; }
  .studio-mark .name {
    font-family: "Mulish", sans-serif; font-weight: 400; font-size: 13px;
    color: var(--navy); line-height: 1.15;
  }

  /* Spine */
  .spine { left: 579px; top: 0; width: 41px; height: 874px; background: var(--navy); }
  .spine-title, .spine-author {
    position: absolute; left: 50%; white-space: nowrap; color: var(--mustard);
  }
  .spine-title {
    top: 200px; transform: translate(-50%, -50%) rotate(90deg);
    font-family: "Montserrat", sans-serif; font-weight: 800; font-size: 24px; letter-spacing: -.5px;
  }
  .spine-author {
    top: 760px; transform: translate(-50%, -50%) rotate(90deg);
    font-family: "Oswald", sans-serif; font-weight: 700; font-size: 24px;
  }

  /* Front cover */
  .front-emblem { left: 814px; top: 33px; width: 150px; height: 180px; }
  .front-title {
    left: 621px; width: 579px; top: 218px; margin: 0; text-align: center;
    font-family: "Montserrat", sans-serif; font-weight: 800; color: var(--navy);
    line-height: .86; letter-spacing: -4px;
  }
  .front-title .word-top { display: block; font-size: 172px; }
  .front-title .word-bottom { display: block; font-size: 112px; letter-spacing: -4px; }
  .subtitle { left: 621px; top: 606px; margin: 0; }
  .subtitle .line {
    display: block; height: 36px; margin-bottom: 3px; box-sizing: border-box;
    padding: 0 8px 0 83px; line-height: 36px; width: max-content;
    font-family: "Raleway", sans-serif; font-weight: 700; font-size: 27px; letter-spacing: -.3px;
  }
  .subtitle .on-light { background: var(--white); color: var(--navy); }
  .subtitle .on-dark { background: var(--navy); color: var(--mustard); }
  .front-author {
    left: 621px; width: 579px; top: 790px; text-align: center; margin: 0;
    font-family: "Oswald", sans-serif; font-weight: 700; font-size: 52px; color: var(--navy);
    letter-spacing: -.5px;
  }
</style>
</head>
<body>
<div class="cover">

  <!-- Back cover -->
  <div class="abs back-emblem" role="img" aria-label="Small illustration of an open head with gears and a light bulb" style="background: var(--navy); border-radius: 40% 40% 20% 20%;"></div>
  <div class="abs back-title"><span class="word-top">Rise</span><span class="word-bottom">Forward</span></div>

  <div class="abs intro">
    <p>My intention is to take you on a journey to help you to understand what is going on in your mind so that you get out from anything that is holding you back in your life. My intention is to guide you to start fully living and experiencing a life that your mind even have yet conceived. To experience a life where you live fearless and without suffering. Living your life where you are the navigator and the creator of how you are experiencing it and you are living in a world of possibilities where there are no limitations.</p>
    <p>For it, we will start to understand more about the mind and about the brain. I am not a neuroscientist and neither I consider my self an expert in the workings of the brain, what I know is the result of my fascination about our brain. This curiosity and the part of me that likes to understand how things work took me to read, research and learn about how our brain works and how its intrinsic mechanisms are subconsciously influencing and limiting us. I encourage you to stay on this part, it can be a bit technical, but understanding how it works will empower you not to allow your mind to dictate the way you approach your life and to live on autopilot.</p>
  </div>

  <div class="abs divider"></div>
  <h2 class="abs about-heading">ABOUT THE AUTHOR</h2>

  <div class="abs author-photo" role="img" aria-label="Portrait photograph of the author" style="background: linear-gradient(160deg, #d9d4cc 0%, #8a6a5e 55%, #c0282c 100%);"></div>
  <p class="abs bio">Daniel Harwood is a high-profile executive coach, professor and Christian leader based in the New York area. Harwood’s commitment to his Christian faith goes deep and spans his entire lifetime. He has served as an executive at the Alder Center for Faith Living, coached clergymen, and has served for 30 years as a Catechist in his local parish. He has been a featured speaker at numerous congregations of all denominations as well as national conferences including Northbridge Business School’s “Dean’s Conference on Leadership, Values, and Spirituality.”</p>

  <div class="abs studio-mark"><span class="dot"></span><span class="name">Larkspur<br>Studio</span></div>

  <!-- Spine -->
  <div class="abs spine">
    <span class="spine-title">Rise Forward</span>
    <span class="spine-author">MARISOL QUINTERO</span>
  </div>

  <!-- Front cover -->
  <div class="abs front-emblem" role="img" aria-label="Illustration of an open head in profile with brain, gears and a glowing light bulb" style="background: linear-gradient(180deg, var(--mustard) 0%, var(--mustard) 30%, var(--navy) 30%, var(--navy) 100%); border-radius: 45% 45% 25% 25%;"></div>

  <h1 class="abs front-title"><span class="word-top">Rise</span><span class="word-bottom">Forward</span></h1>

  <p class="abs subtitle">
    <span class="line on-light">LEAVE BEHIND OLD PATTERNS,</span>
    <span class="line on-dark">QUIT DRIFTING THROUGH DAYS</span>
    <span class="line on-light">AND BEGIN SHAPING</span>
    <span class="line on-dark">EACH MORNING</span>
  </p>

  <p class="abs front-author">MARISOL QUINTERO</p>
</div>
</body>
</html>
```